Hello - we need a label design for our Quillon Health Hair Loss supplement. It is a natural hair loss supplement for black/african american women to regrow new hair and help restore hair loss & thinning hair due to vitamin deficiencies, traction alopecia, etc. It is a science based efficacious supplement with a centuries old medicinal herbal formula.
Attached is the logo & files of other generic competition and also Black hair products for your perusal. The label has to be a upscale and have an ethnic flair to it. The product is clinically effective, leveraged by Ancient Wisdom and Modern Science. The front of the label should include the following:
Quillon Health (logo)
Crown Revitalizer
Advanced Women’s Hair Loss Formula
TRACTION ALOPECIA THERAPY
- Prevents hair loss & restores thinning, fragile hair
- Promotes Natural Hair Growth
- Strengthens Hair for less breakage
- Visibly increases hair density & thickness
- Thicker, Stronger, Longer, Hydrated hair
- Promotes Follicle regeneration & Hair Growth
Site-Specific for hair loss & stunted growth
60 capsules 30-day supply
Target Market(s)
Black/African American Women
Look and feel

```html
<!DOCTYPE html>
<html lang="en">
<head>
<meta charset="utf-8">
<title>Quillon Health Crown Revitalizer – Label</title>
<link rel="stylesheet" href="https://fonts.googleapis.com/css2?family=Archivo+Black&family=Archivo+Narrow:wght@400;600;700&family=Libre+Franklin:wght@700;900&family=Montserrat:wght@500;600;700;800&display=swap">
<style>
  :root {
    --stage: #e6e7e8;
    --ink: #141414;
    --panel-dark: #1b1b1d;
    --white: #ffffff;
    --copper: #a86a3e;
    --copper-light: #d9a574;
    --grey-veil: rgba(205, 205, 210, 0.78);
    --text-grey: #2a2a2a;
  }
  * { box-sizing: border-box; margin: 0; padding: 0; }
  html, body { width: 1096px; height: 1200px; overflow: hidden; background: var(--stage); }
  .label {
    position: absolute; left: 28px; top: 418px;
    width: 1040px; height: 363px; overflow: hidden;
    background: var(--panel-dark);
    box-shadow: 0 6px 14px rgba(0,0,0,0.35);
    font-family: "Montserrat", sans-serif; color: var(--ink);
  }
  .label-bg { position: absolute; inset: 0; }

  /* Back panel */
  .info-panel {
    position: absolute; left: 15px; top: 64px; width: 296px; height: 187px;
    background: var(--grey-veil); text-align: center; padding: 11px 12px 0;
  }
  .info-panel h2 { font-size: 14px; font-weight: 800; margin-bottom: 4px; }
  .info-panel p { font-size: 7.4px; font-weight: 600; line-height: 1.35; color: var(--text-grey); margin-bottom: 7px; }
  .code-block { position: absolute; left: 28px; top: 270px; width: 139px; height: 66px; background: #000; }
  .badge { position: absolute; width: 56px; text-align: center; font-family: "Archivo Narrow", sans-serif; font-size: 7.5px; font-weight: 600; }
  .badge .seal { display: block; width: 22px; height: 22px; margin: 0 auto 2px; border-radius: 50%; border: 2px solid var(--ink); }
  .badge .seal.filled { background: var(--ink); }

  /* Front panel */
  .front { position: absolute; left: 337px; top: 0; width: 360px; height: 363px; text-align: center; }
  .brand { position: absolute; top: 52px; left: 0; right: 0; font-size: 20px; font-weight: 500; color: var(--copper); letter-spacing: 0.5px; }
  .product-name { position: absolute; top: 95px; left: 0; right: 0; font-family: "Archivo Black", sans-serif; font-size: 33px; line-height: 37px; color: var(--ink); font-weight: 400; }
  .ribbon-copper {
    position: absolute; top: 175px; left: 24px; width: 312px; height: 20px;
    background: linear-gradient(90deg, var(--copper), var(--copper-light) 50%, var(--copper));
    clip-path: polygon(0 0, 100% 0, 97% 100%, 3% 100%);
    font-size: 12.5px; font-weight: 700; line-height: 20px; color: var(--ink);
  }
  .ribbon-black {
    position: absolute; top: 198px; left: 59px; width: 242px; height: 17px;
    background: var(--ink); border-radius: 0 0 10px 10px;
    font-size: 11.5px; font-weight: 700; line-height: 17px; color: var(--white); letter-spacing: 0.3px;
  }
  .benefits { position: absolute; top: 230px; left: 34px; width: 300px; display: grid; grid-template-columns: 146px 146px; column-gap: 8px; row-gap: 1px; list-style: none; text-align: left; }
  .benefits li { display: flex; gap: 5px; font-size: 7.6px; font-weight: 700; line-height: 1.2; height: 21px; }
  .benefits svg { flex: none; width: 12px; height: 12px; }
  .tagline { position: absolute; top: 296px; left: 0; right: 0; font-size: 12.5px; font-weight: 700; }
  .supply-bar { position: absolute; top: 325px; left: 59px; width: 242px; height: 40px; background: var(--ink); border-radius: 14px 14px 0 0; color: var(--white); }
  .supply-bar .count { position: absolute; top: 6px; font-size: 24px; font-weight: 800; line-height: 24px; }
  .supply-bar .count small { font-size: 8px; font-weight: 700; vertical-align: middle; }
  .supply-bar .count.capsules { left: 18px; }
  .supply-bar .count.days { left: 148px; }
  .supply-bar .count.days small { display: inline-block; line-height: 8px; vertical-align: middle; text-align: left; }
  .supply-bar .emblem { position: absolute; left: 100px; top: -3px; width: 42px; height: 42px; border-radius: 50%; background: var(--white); border: 3px solid var(--ink); }

  /* Nutrition facts */
  .nutrition {
    position: absolute; left: 760px; top: 64px; width: 256px; height: 267px; overflow: hidden;
    background: var(--white); border: 1px solid var(--ink); padding: 3px 5px;
    font-family: "Archivo Narrow", sans-serif; font-size: 6.4px; line-height: 1.2; color: var(--ink);
  }
  .nutrition h3 { font-family: "Libre Franklin", sans-serif; font-weight: 900; font-size: 27px; line-height: 29px; letter-spacing: -0.3px; border-bottom: 1px solid var(--ink); }
  .nf-row { display: flex; justify-content: space-between; border-bottom: 0.7px solid var(--ink); padding: 0.5px 0; }
  .nf-row.plain { border: none; }
  .nf-row.serving { font-size: 7.8px; font-weight: 700; border-bottom: 6px solid var(--ink); padding-bottom: 2px; }
  .nf-small { font-size: 4.8px; font-weight: 700; }
  .nf-calories { display: flex; justify-content: space-between; align-items: flex-end; font-family: "Libre Franklin", sans-serif; font-weight: 700; font-size: 12.5px; line-height: 14px; border-bottom: 3.5px solid var(--ink); }
  .nf-calories span:last-child { font-size: 18px; line-height: 18px; }
  .nf-dv { text-align: right; font-size: 4.8px; font-weight: 700; border-bottom: 0.7px solid var(--ink); }
  .nf-row b { font-weight: 700; }
  .i1 { padding-left: 10px !important; }
  .i3 { padding-left: 30px !important; }
  .nf-row.thick { border-bottom: 4px solid var(--ink); }
  .nf-row.last { border-bottom: 3px solid var(--ink); }
  .nf-foot { font-size: 4.6px; line-height: 1.25; padding-top: 2px; }
</style>
</head>
<body>
<div class="label">
  <svg class="label-bg" viewBox="0 0 1040 363" preserveAspectRatio="none" aria-hidden="true">
    <defs>
      <linearGradient id="copperBand" x1="0" y1="0" x2="1" y2="1">
        <stop offset="0" stop-color="#7a4a2a"/>
        <stop offset="0.5" stop-color="#c7925f"/>
        <stop offset="1" stop-color="#6b3f22"/>
      </linearGradient>
      <linearGradient id="goldBand" x1="0" y1="0" x2="1" y2="1">
        <stop offset="0" stop-color="#e2cfa8"/>
        <stop offset="1" stop-color="#a88a5c"/>
      </linearGradient>
    </defs>
    <rect width="1040" height="363" fill="#1b1b1d"/>
    <polygon points="300,0 400,0 0,300 0,240" fill="url(#goldBand)" opacity="0.85"/>
    <polygon points="220,0 280,0 0,210 0,170" fill="url(#copperBand)" opacity="0.75"/>
    <polygon points="600,0 700,0 1040,270 1040,320" fill="url(#copperBand)"/>
    <polygon points="740,0 800,0 1040,160 1040,200" fill="url(#goldBand)" opacity="0.55"/>
    <polygon points="0,285 330,232 362,112 478,12 556,12 672,112 704,232 1040,305 1040,363 0,363" fill="#ffffff"/>
    <polygon points="440,0 594,0 517,52" fill="#c9cbd0"/>
  </svg>

  <section class="info-panel">
    <h2>Headline</h2>
    <p>Lorem ipsum dolor sit amet, consectetuer adipiscing elit, sed diam nonummy nibh euismod tincidunt ut laoreet dolore magna aliquam erat volutpat. Ut wisi enim ad minim veniam, quis nostrud exerci tation ullamcorper suscipit lobortis nisl ut aliquip ex ea commodo consequat. Duis autem vel eum iriure dolor in hendrerit in vulputate velit esse molestie consequat.</p>
    <p>Lorem ipsum dolor sit amet, consectetuer adipiscing elit, sed diam nonummy nibh euismod tincidunt ut laoreet dolore magna aliquam erat volutpat. Ut wisi enim ad minim veniam, quis nostrud exerci tation ullamcorper suscipit lobortis nisl ut aliquip ex ea commodo consequat. Duis autem vel eum iriure dolor in hendrerit in vulputate velit esse molestie consequat.</p>
  </section>
  <div class="code-block"></div>
  <div class="badge" style="left:189px;top:259px"><span class="seal"></span>Gluten Free</div>
  <div class="badge" style="left:243px;top:259px"><span class="seal"></span>Kosher Certified</div>
  <div class="badge" style="left:189px;top:301px"><span class="seal"></span>Lactose Free</div>
  <div class="badge" style="left:243px;top:301px"><span class="seal filled"></span>Non GMO</div>

  <section class="front">
    <div class="brand">Quillon Health</div>
    <h1 class="product-name">CROWN<br>REVITALIZER</h1>
    <div class="ribbon-copper">Advanced Women’s Hair Loss Formula</div>
    <div class="ribbon-black">TRACTION ALOPECIA THERAPY</div>
    <ul class="benefits">
      <li><svg viewBox="0 0 14 14"><circle cx="7" cy="7" r="5.5" fill="none" stroke="#a86a3e" stroke-width="1.3"/><path d="M4 7l2.3 2.3L12 2.5" fill="none" stroke="#a86a3e" stroke-width="1.6"/></svg>Prevents hair loss &amp; restores thinning, fragile hair</li>
      <li><svg viewBox="0 0 14 14"><circle cx="7" cy="7" r="5.5" fill="none" stroke="#a86a3e" stroke-width="1.3"/><path d="M4 7l2.3 2.3L12 2.5" fill="none" stroke="#a86a3e" stroke-width="1.6"/></svg>Visibly increases hair density &amp; thickness</li>
      <li><svg viewBox="0 0 14 14"><circle cx="7" cy="7" r="5.5" fill="none" stroke="#a86a3e" stroke-width="1.3"/><path d="M4 7l2.3 2.3L12 2.5" fill="none" stroke="#a86a3e" stroke-width="1.6"/></svg>Promotes Natural Hair Growth</li>
      <li><svg viewBox="0 0 14 14"><circle cx="7" cy="7" r="5.5" fill="none" stroke="#a86a3e" stroke-width="1.3"/><path d="M4 7l2.3 2.3L12 2.5" fill="none" stroke="#a86a3e" stroke-width="1.6"/></svg>Thicker, Stronger, Longer, Hydrated hair</li>
      <li><svg viewBox="0 0 14 14"><circle cx="7" cy="7" r="5.5" fill="none" stroke="#a86a3e" stroke-width="1.3"/><path d="M4 7l2.3 2.3L12 2.5" fill="none" stroke="#a86a3e" stroke-width="1.6"/></svg>Strengthens Hair for less breakage</li>
      <li><svg viewBox="0 0 14 14"><circle cx="7" cy="7" r="5.5" fill="none" stroke="#a86a3e" stroke-width="1.3"/><path d="M4 7l2.3 2.3L12 2.5" fill="none" stroke="#a86a3e" stroke-width="1.6"/></svg>Promotes Follicle regeneratio &amp; Hair Growth</li>
    </ul>
    <div class="tagline">Site-Specific for hair loss &amp; stunted growth</div>
    <div class="supply-bar">
      <span class="count capsules">60 <small>capsules</small></span>
      <span class="emblem" role="img" aria-label="Hair follicle emblem"></span>
      <span class="count days">30 <small>day<br>supply</small></span>
    </div>
  </section>

  <section class="nutrition">
    <h3>Nutrition Facts</h3>
    <div class="nf-row plain">4 servings per container/6 raciones por envase</div>
    <div class="nf-row serving"><span>Serving size/Tamaño de la porción</span><span>1 cup/1 taza (180g)</span></div>
    <div class="nf-small">Amount per serving/Cantidad por porción</div>
    <div class="nf-calories"><span>Calories/Calorías</span><span>245</span></div>
    <div class="nf-dv">% Daily Value*/% Valor diario*</div>
    <div class="nf-row"><span><b>Total Fat/Grasa total</b> 12g</span><b>14%</b></div>
    <div class="nf-row i1"><span>Saturated Fat/Grasa Saturada 2g</span><b>10%</b></div>
    <div class="nf-row i1"><span><i>Trans</i> Fat/Grasa <i>Trans</i> 0g</span><span></span></div>
    <div class="nf-row"><span><b>Cholesterol/Colesterol</b> 8mg</span><b>3%</b></div>
    <div class="nf-row"><span><b>Sodium/Sodio</b> 210mg</span><b>9%</b></div>
    <div class="nf-row"><span><b>Total Carbohydrate/Carbohidrato Total</b> 34g</span><b>12%</b></div>
    <div class="nf-row i1"><span>Dietary Fiber/Fibra Dietética 7g</span><b>25%</b></div>
    <div class="nf-row i1"><span>Total Sugars/Azúcares Totales 5g</span><span></span></div>
    <div class="nf-row i3"><span>Includes 4g Added Sugars/Incluye 4 g de azúcares añadidos</span><b>8%</b></div>
    <div class="nf-row thick"><span><b>Protein/Proteínas</b> 11g</span><span></span></div>
    <div class="nf-row"><span>Vitamin D/Vitamina D 4mcg</span><span>20%</span></div>
    <div class="nf-row"><span>Calcium/Calcio 210mg</span><span>16%</span></div>
    <div class="nf-row"><span>Iron/Hierro 3mg</span><span>15%</span></div>
    <div class="nf-row last"><span>Potassium/Potasio 380mg</span><span>8%</span></div>
    <p class="nf-foot">* The % Daily Value (DV) tells you how much a nutrient in a serving of food contributes to a daily diet. 2,000 calories a day is used for general nutrition advice.</p>
  </section>
</div>
</body>
</html>
```